eCommerce website for a DIY shop & communal center

We need a website for a business called The Maker Loft. The Maker Loft is both a shop and communal establishment where people with shared interests, especially in DIY (Do It Yourself) and crafting, can gather to shop for & work on projects while sharing ideas, equipment, supplies and knowledge. The shop is both brick & motor and online. The physical communal space provides workstations, equipment, tools and supplies and expertise for DIY lovers to create their projects.

Target Market(s)

Middle & upper class DIY enthusiasts, creative hobbyists, budding artists & small business owners

Industry/Entity Type

DIY, Arts & Crafts

Coding

Coded - Design and coding required

Number of Pages Required

5+ page

Requirements
Must have
• Menus to include 1. home page (with about us, operating hours, contacts, location, meet the team); 2. Studio activities (how to DIY at the Studio, booking, equipment & tools, house rules); 3. Studio events (events in the Studio, offsite events); 4. Resources (FAQs, tutorials, blogs, eBooks) and 5. Online shop
Nice to have
• Branding guidelines eg logo colours (see attachment) to influence design. Woo commerce shop. Booking feature for activities & events at the Studio.

```html
<!DOCTYPE html>
<html lang="en">
<head>
<meta charset="utf-8">
<title>The Maker Loft</title>
<link href="https://fonts.googleapis.com/css2?family=Cinzel:wght@400;600;700&family=Roboto:wght@400;500;700&display=swap" rel="stylesheet">
<style>
:root{
  --teal:#34b4b7;
  --coral:#f2564c;
  --ink:#111;
  --muted:#7a7a7a;
  --dark:#1e1e1e;
  --white:#fff;
}
*{margin:0;padding:0;box-sizing:border-box}
html,body{width:1200px;height:3854px;overflow:hidden}
body{position:relative;font-family:"Roboto",sans-serif;color:var(--ink);background:var(--white)}
.abs{position:absolute}
.serif{font-family:"Cinzel",serif}
.btn{position:absolute;height:54px;border-radius:27px;color:#fff;font:700 13px "Roboto",sans-serif;display:flex;align-items:center;justify-content:center;letter-spacing:.2px;box-shadow:5px -1px 0 var(--coral)}
.btn.teal{background:var(--teal)}
.btn.coral{background:var(--coral);box-shadow:5px -1px 0 #fff}

/* hero */
.hero{left:0;top:0;width:1200px;height:634px;background:linear-gradient(135deg,#3e4a48 0%,#8a7a6a 40%,#c9b9a5 70%,#b0634c 100%)}
.hero-shade{left:0;top:0;width:1200px;height:160px;background:linear-gradient(#14302ecc,transparent)}
.logo{left:145px;top:48px;font:600 36px "Cinzel",serif;color:#fff;letter-spacing:1px}
.nav{left:507px;top:60px;display:flex;gap:31px;font:700 13px "Roboto",sans-serif;color:#fff}
.nav span{position:relative}
.nav .active::after{content:"";position:absolute;left:-4px;right:-4px;top:24px;height:3px;background:var(--coral)}
.hero-title{left:0;width:1200px;top:240px;text-align:center;font:600 92px "Cinzel",serif;color:#fff}
.dots{left:569px;top:552px;display:flex;gap:9px}
.dots i{width:9px;height:9px;border-radius:50%;background:#fff}
.dots i.on{background:var(--coral)}

/* about */
.about-back{left:93px;top:738px;width:300px;height:420px;background:var(--coral);border-radius:200px 0 0 0}
.about-photo{left:118px;top:748px;width:382px;height:416px;border-radius:170px 190px 190px 0;background:linear-gradient(140deg,#5a3b24,#a66a3a 50%,#d79a5c)}
.h2{font:700 56px "Cinzel",serif;color:var(--ink)}
.about-h{left:558px;top:748px}
.about-text{left:558px;top:836px;width:500px;font-size:13px;line-height:25px;color:var(--muted)}
.about-text p+p{margin-top:24px}

/* team */
.team-h{left:0;width:1200px;top:1334px;text-align:center}
.member{top:1468px;width:240px}
.member .ring{width:240px;height:240px;border-radius:50%;border:4px solid var(--teal);padding:21px}
.member .face{width:100%;height:100%;border-radius:50%}
.member h3{margin-top:30px;text-align:center;font:400 20px "Roboto",sans-serif;color:var(--coral)}
.member p{margin-top:10px;text-align:center;font-size:14px;line-height:22px}

/* events */
.events-bg{left:0;top:2050px}
.events-h{left:0;width:1200px;top:2176px;text-align:center;color:#fff}
.card{top:2300px;width:288px;color:#fff}
.card .pic{height:167px}
.card h4{margin-top:28px;font:500 18px "Roboto",sans-serif;line-height:25px}
.card p{margin-top:14px;font-size:12.5px;line-height:20px}
.arrow{top:2365px;width:40px;height:40px;border:2px solid #fff;border-radius:50%;display:flex;align-items:center;justify-content:center}
.map-frame{left:175px;top:2853px;width:850px;height:460px;background:#fff;border-radius:12px 12px 0 0;padding:15px 15px 0}
.map{width:100%;height:100%;background:linear-gradient(160deg,#a9a9a9,#8d8d8d 50%,#9f9f9f)}

/* contacts */
.contacts-h{left:0;width:1200px;top:3392px;text-align:center}
.c-item{display:flex;align-items:center;gap:17px;font-size:13px;line-height:21px;color:#333}
.c-icon{width:60px;height:60px;border-radius:50%;display:flex;align-items:center;justify-content:center;flex:none}
.c-icon.teal{background:var(--teal)}
.c-icon.coral{background:var(--coral)}

/* footer */
.footer{left:0;top:3762px;width:1200px;height:92px;background:var(--dark);color:#fff;font-size:13px}
.footer .copy{position:absolute;left:144px;top:38px}
.footer .social{position:absolute;right:144px;top:36px;display:flex;gap:10px}
.footer .social i{width:16px;height:16px;border-radius:50%;background:#fff}
</style>
</head>
<body>

<section class="hero abs" role="img" aria-label="Photo of hands threading colourful beads from a sorted bead box"></section>
<div class="hero-shade abs"></div>
<svg class="abs" style="left:0;top:0" width="1200" height="634"><path d="M0 340 C90 520 330 634 760 634 L0 634 Z" fill="#fff"/></svg>
<div class="logo abs">Maker Loft</div>
<nav class="nav abs"><span class="active">HOME</span><span>STUDIO ACTIVITIES</span><span>STUDIO EVENTS</span><span>RESOURCES</span><span>ONLINE SHOP</span></nav>
<h1 class="hero-title abs">MAKER LOFT</h1>
<div class="btn teal" style="left:497px;top:385px;width:200px">BOOKING ACTIVITIES</div>
<div class="dots abs"><i></i><i></i><i class="on"></i><i></i></div>

<div class="about-back abs"></div>
<div class="about-photo abs" role="img" aria-label="Photo of a father and child building a wooden birdhouse"></div>
<h2 class="h2 about-h abs">ABOUT US</h2>
<div class="about-text abs">
<p>The Maker Loft is both a shop and communal establishment where people with shared interests especially in DIY (Do It Yourself) and crafting, can gather to shop for &amp; work on projects while sharing ideas, equipment, supplies and knowledge.</p>
<p>Lorem ipsum dolor sit amet, consectetur adipiscing elit, sed do eiusmod tempor incididunt ut labore et dolore magna aliquais ipsum suspendisse ultrices gravida. Risus commodo viverra maecenas accumsan lacus vel facilisisorem ipsum dolor sit amet, consectetur adipiscing elit, sed do eiusmod tempor incididunt ut labore et dolore magna aliquais ipsum suspendisse ultrices gravida</p>
</div>
<div class="btn teal" style="left:558px;top:1090px;width:168px">READ MORE</div>

<h2 class="h2 team-h abs">MEET THE TEAM</h2>
<div class="member abs" style="left:144px"><div class="ring"><div class="face" role="img" aria-label="Portrait of team member Tom Arden" style="background:linear-gradient(160deg,#3c4a55,#7c8ea3)"></div></div><h3>TOM ARDEN</h3><p>Sed ut perspiciatis unmnis<br>iste natus</p></div>
<div class="member abs" style="left:480px"><div class="ring"><div class="face" role="img" aria-label="Portrait of team member Lena Pratt" style="background:linear-gradient(160deg,#c9b7a4,#e9ddd0)"></div></div><h3>LENA PRATT</h3><p>Sed ut perspiciatis unmnis<br>iste natus</p></div>
<div class="member abs" style="left:816px"><div class="ring"><div class="face" role="img" aria-label="Portrait of team member Mark Voss" style="background:linear-gradient(160deg,#d8dde2,#2b3446)"></div></div><h3>MARK VOSS</h3><p>Sed ut perspiciatis unmnis<br>iste natus</p></div>
<div class="btn teal" style="left:513px;top:1885px;width:168px">VIEW MORE</div>

<svg class="events-bg abs" width="1200" height="960"><path d="M0 0 H760 C990 0 1200 170 1200 360 V820 C1150 880 1080 930 1025 960 L175 960 C90 890 30 810 0 700 Z" fill="var(--teal)"/></svg>
<h2 class="h2 events-h abs">STUDIO EVENTS</h2>
<div class="arrow abs" style="left:85px"><svg width="14" height="14"><path d="M9 2 L4 7 L9 12" stroke="#fff" stroke-width="2" fill="none"/></svg></div>
<div class="arrow abs" style="left:1075px"><svg width="14" height="14"><path d="M5 2 L10 7 L5 12" stroke="#fff" stroke-width="2" fill="none"/></svg></div>
<div class="card abs" style="left:143px"><div class="pic" role="img" aria-label="Photo of hands weaving with yarn and macrame cord" style="background:linear-gradient(135deg,#d9cfc0,#6fa3b3)"></div><h4>Nemo enim ipsam voluptem quia voluptas</h4><p>Lorem ipsum dolor sit amet, consectetur adipiscing elit, sed do eiusmod tempor incididuntcommodo viverra</p></div>
<div class="card abs" style="left:455px"><div class="pic" role="img" aria-label="Photo of a clay vase being shaped on a pottery wheel" style="background:linear-gradient(135deg,#3a2516,#a56b3c 60%,#6c8f95)"></div><h4>Ut enim ad minima veniam quis nostrum</h4><p>Lorem ipsum dolor sit amet, consectetur adipiscing elit, sed do eiusmod tempor incididuntcommodo viverra</p></div>
<div class="card abs" style="left:767px"><div class="pic" role="img" aria-label="Photo of paper craft flowers and cutouts on a table" style="background:linear-gradient(135deg,#2d4a3c,#b02d3a 60%,#e3d7c4)"></div><h4>Nemo enim ipsam voluptem quia voluptas</h4><p>Lorem ipsum dolor sit amet, consectetur adipiscing elit, sed do eiusmod tempor incididuntcommodo viverra</p></div>
<div class="btn coral" style="left:143px;top:2657px;width:168px">BOOK NOW</div>
<div class="btn coral" style="left:455px;top:2657px;width:168px">BOOK NOW</div>
<div class="btn coral" style="left:767px;top:2657px;width:168px">BOOK NOW</div>

<div class="map-frame abs"><div class="map" role="img" aria-label="Grey location map showing the studio pin"></div></div>
<svg class="abs" style="left:553px;top:3106px" width="24" height="34"><path d="M12 0 C5 0 0 5 0 12 C0 21 12 34 12 34 C12 34 24 21 24 12 C24 5 19 0 12 0 Z" fill="#e53935"/><circle cx="12" cy="12" r="4.5" fill="#fff"/></svg>

<h2 class="h2 contacts-h abs">CONTACTS</h2>
<div class="c-item abs" style="left:320px;top:3523px"><div class="c-icon teal"><svg width="18" height="24"><path d="M9 1 C4.5 1 1 4.5 1 9 C1 15 9 23 9 23 C9 23 17 15 17 9 C17 4.5 13.5 1 9 1 Z" fill="#fff"/><circle cx="9" cy="9" r="3" fill="var(--teal)"/></svg></div><div>122,Lorem ipsum dolor smetons<br>ectetur adipiscing elit</div></div>
<div class="c-item abs" style="left:620px;top:3523px"><div class="c-icon coral"><svg width="22" height="22" viewBox="0 0 24 24"><path d="M6.6 10.8a15 15 0 0 0 6.6 6.6l2.2-2.2c.3-.3.7-.4 1-.2 1.1.4 2.3.6 3.6.6.6 0 1 .4 1 1V20c0 .6-.4 1-1 1A17 17 0 0 1 3 4c0-.6.4-1 1-1h3.5c.6 0 1 .4 1 1 0 1.3.2 2.5.6 3.6.1.3 0 .7-.2 1z" fill="#fff"/></svg></div><div>Phone : 1 555 010 0199</div></div>
<div class="c-item abs" style="left:320px;top:3617px"><div class="c-icon coral"><svg width="24" height="18"><rect x="1" y="1" width="22" height="16" rx="2" fill="#fff"/><path d="M2 3 L12 10 L22 3" stroke="var(--coral)" stroke-width="2" fill="none"/></svg></div><div>Email : info@makerloft.example</div></div>
<div class="c-item abs" style="left:620px;top:3617px"><div class="c-icon teal"><svg width="24" height="24"><circle cx="12" cy="12" r="9" stroke="#fff" stroke-width="2.4" fill="none"/><path d="M12 7 V12 L15 14" stroke="#fff" stroke-width="2.2" fill="none"/></svg></div><div>Opening Hours<br>Mon -&nbsp; Sat : 09:00am to 08:00pm</div></div>

<footer class="footer abs">
  <div class="copy">© 2021 The Maker Loft. All rights reserved.Privacy &nbsp;|&nbsp; Terms of Use</div>
  <div class="social"><i></i><i></i><i></i></div>
</footer>
</body>
</html>
```